Logo is done, need templates now

I want to be able to have an email template, same for word documents, powerpoint etc. I have the logo, now I need all the pieces for appearance in correspondence and marketing

Target Market(s)

Professional Advisors and Wealthy Clients

Font styles to use
Serif

Requirements
Must have
• I want to be able to do word documents and email them with letterhead. I need great email signatures. I need similar formatting for the word documents to be flexible to add to powerpoint and other presentations.

```html
<!DOCTYPE html>
<html lang="en">
<head>
<meta charset="utf-8">
<title>Silvane Capital – Stationery</title>
<link rel="stylesheet" href="https://fonts.googleapis.com/css2?family=Lato:wght@400;700&display=swap">
<style>
  :root {
    --backdrop: #5e5e5e;
    --paper: #ffffff;
    --gold: #b8874a;
    --gold-light: #d2a56c;
    --gold-dark: #8f6432;
    --band: #242424;
    --ink: #1b1b1b;
    --rule: #d6d6d6;
  }
  * { box-sizing: border-box; margin: 0; padding: 0; }
  html, body { width: 800px; height: 1200px; overflow: hidden; }
  body {
    background: var(--backdrop);
    font-family: "Lato", Arial, sans-serif;
    color: var(--ink);
    position: relative;
  }

  /* Letterhead */
  .letterhead {
    position: absolute; left: 145.6px; top: 116.8px;
    width: 508.8px; height: 761.6px;
    background: var(--paper); overflow: hidden;
  }
  .brand {
    position: absolute; display: flex; flex-direction: column; align-items: center;
  }
  .brand__dot {
    width: 16px; height: 16px; border-radius: 50%;
    background: var(--gold); margin-bottom: 12px;
  }
  .brand__name {
    font-weight: 400; color: var(--gold);
    text-transform: uppercase; white-space: nowrap;
  }
  .letterhead .brand { left: 36px; top: 34px; width: 160px; }
  .letterhead .brand__name { font-size: 11.5px; letter-spacing: 3.6px; }

  .contact-block {
    position: absolute; left: 335px; top: 21.6px; height: 38.4px;
    border-left: 1px solid var(--rule); padding-left: 16px;
    font-size: 10.4px; line-height: 12.8px; padding-top: 1px;
  }
  .contact-block b { font-weight: 700; }

  .footer-band {
    position: absolute; left: 0; bottom: 0;
  }
  .footer-band__address {
    position: absolute; color: var(--gold-light); white-space: nowrap;
  }
  .letterhead .footer-band { width: 508.8px; height: 56px; }
  .letterhead .footer-band__address { left: 58.4px; bottom: 7px; font-size: 10.4px; }

  .footer-band svg { position: absolute; left: 0; top: 0; }

  /* Email signature */
  .signature {
    position: absolute; left: 145.6px; top: 966.4px;
    width: 508.8px; height: 152px;
    background: var(--paper); overflow: hidden;
  }
  .signature__details { position: absolute; left: 20.8px; top: 37px; }
  .signature__name { font-size: 16px; font-weight: 700; color: var(--gold); line-height: 18px; }
  .signature__role { font-size: 12px; line-height: 14px; }
  .signature__line { font-size: 12.4px; line-height: 15.6px; }
  .signature__line:first-of-type { margin-top: 8px; }
  .signature__line b { font-weight: 700; }
  .social {
    position: absolute; left: 19.2px; top: 107px;
    display: flex; align-items: center; gap: 2px; font-size: 12px;
  }
  .social__label { margin-right: 5px; }
  .social__dot { width: 17px; height: 17px; border-radius: 50%; background: var(--gold); }
  .social__handle { margin-left: 4px; color: #444; }
  .signature .brand { left: 326px; top: 28px; width: 150px; }
  .signature .brand__dot { width: 14px; height: 14px; margin-bottom: 12px; }
  .signature .brand__name { font-size: 11px; letter-spacing: 3.4px; }
  .signature .footer-band { width: 508.8px; height: 37px; }
  .signature .footer-band__address { left: 22.4px; bottom: 5px; font-size: 12.8px; }
</style>
</head>
<body>

<section class="letterhead" aria-label="Letterhead">
  <div class="brand">
    <span class="brand__dot"></span>
    <span class="brand__name">Silvane Capital</span>
  </div>
  <div class="contact-block">
    <p><b>P:</b> 044-987 654 321</p>
    <p><b>E:</b> info@mailname.com</p>
    <p><b>W:</b> www.yoursitename.com</p>
  </div>
  <div class="footer-band">
    <svg width="508.8" height="56" viewBox="0 0 508.8 56" aria-hidden="true">
      <defs>
        <linearGradient id="goldFade" x1="0" y1="0" x2="1" y2="1">
          <stop offset="0" stop-color="#d2a56c"/>
          <stop offset="1" stop-color="#8f6432"/>
        </linearGradient>
      </defs>
      <polygon points="0,32 414,32 424,56 0,56" fill="var(--band)"/>
      <rect x="448" y="0" width="60.8" height="56" fill="url(#goldFade)"/>
    </svg>
    <span class="footer-band__address">18, Street line here, 20931,Country Name</span>
  </div>
</section>

<section class="signature" aria-label="Email signature">
  <div class="signature__details">
    <p class="signature__name">Adrian Hale</p>
    <p class="signature__role">Managing Director</p>
    <p class="signature__line"><b>P:</b> 044-987 654 321 | <b>E:</b> info@mailname.com</p>
    <p class="signature__line">www.yoursitename.com</p>
  </div>
  <div class="social">
    <span class="social__label">Follow us on:</span>
    <span class="social__dot"></span>
    <span class="social__dot"></span>
    <span class="social__dot"></span>
    <span class="social__dot"></span>
    <span class="social__dot"></span>
    <span class="social__handle">/ name</span>
  </div>
  <div class="brand">
    <span class="brand__dot"></span>
    <span class="brand__name">Silvane Capital</span>
  </div>
  <div class="footer-band">
    <svg width="508.8" height="37" viewBox="0 0 508.8 37" aria-hidden="true">
      <defs>
        <linearGradient id="goldFadeSig" x1="0" y1="0" x2="1" y2="1">
          <stop offset="0" stop-color="#d2a56c"/>
          <stop offset="1" stop-color="#8f6432"/>
        </linearGradient>
      </defs>
      <polygon points="0,14 444.8,14 454,37 0,37" fill="var(--band)"/>
      <rect x="470" y="0" width="38.8" height="37" fill="url(#goldFadeSig)"/>
    </svg>
    <span class="footer-band__address">18, Street line here, 20931,Country Name</span>
  </div>
</section>

</body>
</html>
```